Corvella Paintless Dent Removal

Our company works on vehicles removing dents using a highly skilled trade which the metal is massaged out with special tools without disturbing the original paint, hence paintless dent removal. Besides keeping the paint and metal original its also very environmentally friendly since no paint or toxic fillers are used. Also we we are one of the most experienced companies in the business with 25 years

Target Market(s)

Retail Automobile consumers, Auto Dealerships and Auto Body Shops

Industry/Entity Type

Auto Repair

Contact Information for Business Card

Dennis Holbrook
PO Box 538 Ashmere, NY 11952
631-472-8816
corvellapdr@mailnest.example
website corvellapdr.example
youtube corvella paintless dent removal
25 years of experience removing Dents, Dings and Hail Damage

Font styles to use
Serif
Sans Serif

Colors

Designer to choose colors to be used in the design.

Requirements
Must have
• I do like things that are simple but classy and somewhat bold, also I like my logo so that should be somewhat important

```html
<!DOCTYPE html>
<html lang="en">
<head>
<meta charset="utf-8">
<title>Corvella Paintless Dent Removal – Business Card</title>
<link href="https://fonts.googleapis.com/css2?family=Josefin+Sans:wght@300&family=Oswald:wght@300;400&display=swap" rel="stylesheet">
<style>
  :root {
    --backdrop: #e3e7ea;
    --card: #ffffff;
    --navy: #13284c;
    --green: #7dc142;
    --white: #ffffff;
  }
  html, body {
    margin: 0;
    padding: 0;
    width: 1200px;
    height: 1000px;
    overflow: hidden;
    background: var(--backdrop);
  }
  .card {
    position: absolute;
    left: 180px;
    top: 248px;
    width: 841px;
    height: 503px;
    background: var(--card);
    overflow: hidden;
  }
  .card__band {
    position: absolute;
    left: 0;
    top: 378px;
    width: 100%;
    height: 125px;
    background: var(--green);
  }
  .card__rule {
    position: absolute;
    left: 0;
    top: 370px;
    width: 100%;
    height: 8px;
    background: var(--navy);
  }
  .holder-name {
    position: absolute;
    left: 66px;
    top: 92px;
    margin: 0;
    font-family: "Josefin Sans", sans-serif;
    font-weight: 300;
    font-size: 44px;
    font-variant: small-caps;
    letter-spacing: 1px;
    color: var(--green);
    line-height: 1;
  }
  .contact {
    position: absolute;
    left: 68px;
    top: 146px;
    margin: 0;
    font-family: "Oswald", sans-serif;
    font-weight: 300;
    font-size: 27px;
    line-height: 35px;
    color: var(--navy);
  }
  .contact p { margin: 0; }
  .contact .contact__gap { height: 34px; }
  .brand {
    position: absolute;
    left: 500px;
    top: 78px;
    display: flex;
    align-items: center;
    gap: 14px;
  }
  .brand__dot {
    width: 46px;
    height: 46px;
    border-radius: 50%;
    background: var(--green);
  }
  .brand__name {
    font-family: "Oswald", sans-serif;
    font-weight: 400;
    color: var(--navy);
    line-height: 1.05;
  }
  .brand__name span { display: block; }
  .brand__name .brand__main { font-size: 34px; letter-spacing: 1px; }
  .brand__name .brand__sub { font-size: 18px; }
  .tagline {
    position: absolute;
    left: 66px;
    top: 405px;
    margin: 0;
    font-family: "Oswald", sans-serif;
    font-weight: 400;
    font-size: 25.5px;
    letter-spacing: 0.6px;
    color: var(--white);
    text-transform: uppercase;
    white-space: pre;
  }
</style>
</head>
<body>
  <div class="card">
    <div class="card__band"></div>
    <div class="card__rule"></div>

    <h1 class="holder-name">Dennis Holbrook</h1>

    <div class="contact">
      <p>PO Box 538 Ashmere, NY 11952</p>
      <p>corvellapdr@mailnest.example</p>
      <p>631-472-8816</p>
      <div class="contact__gap"></div>
      <p>Website &nbsp;| corvellapdr.example</p>
      <p>YouTube | corvella paintless dent removal</p>
    </div>

    <div class="brand">
      <div class="brand__dot"></div>
      <div class="brand__name">
        <span class="brand__main">CORVELLA</span>
        <span class="brand__sub">Paintless Dent Removal</span>
      </div>
    </div>

    <p class="tagline">25  Years of Experience Removing Dents, Dings and Hail Damage</p>
  </div>
</body>
</html>
```